Request for Business Card Design

Hi. My name is Marlena, I am looking for a new business card design for my company, Quorvane Sensing Systems, LLC. I really like the design you did for Tessaly Harvest and was hoping you could do something similar using our full logo and our mark. I am also open to any raised texture design using our mark. I have attached our full logo, which would need to be somewhere on the card, as well as the mark in both outline and full form, as well as our brand colors / guide. The card does not have to be white, as long as our logo and mark appear. I actually like darker colored business cards more, but am open to all options. If you are interested in working with me, please let me know. We would also take the business card design into letterhead design if you can do that.

```html
<!DOCTYPE html>
<html lang="en">
<head>
<meta charset="utf-8">
<title>Quorvane Sensing Systems – Business Card</title>
<link rel="stylesheet" href="https://fonts.googleapis.com/css2?family=Roboto:wght@400;700;900&display=swap">
<style>
  :root {
    --stage: #3a3a3a;
    --card: #1d1d1e;
    --ink: #ffffff;
    --ink-soft: #d9d9d9;
    --accent: #0a9ac6;
    --divider: #4a4a4a;
  }
  * { margin: 0; padding: 0; box-sizing: border-box; }
  html, body { width: 1200px; height: 689px; overflow: hidden; }
  body {
    background: var(--stage);
    font-family: "Roboto", Arial, sans-serif;
    color: var(--ink);
    position: relative;
  }
  .card {
    position: absolute;
    top: 190px;
    width: 540px;
    height: 309px;
    background: var(--card);
    border-radius: 18px;
    overflow: hidden;
    box-shadow: 0 18px 40px rgba(0,0,0,.45);
  }
  .card--back { left: 40px; }
  .card--front { left: 620px; }

  /* Back */
  .back-mark {
    position: absolute;
    left: 250px; top: -40px;
    width: 260px; height: 260px;
    border-radius: 50%;
    background: radial-gradient(circle at 40% 35%, #3c3c3e, #1a1a1b 70%);
  }
  .back-name {
    position: absolute;
    left: 40px; bottom: 44px;
    font-weight: 900;
    font-size: 34px;
    letter-spacing: 3px;
    line-height: 1;
  }
  .back-tagline {
    position: absolute;
    left: 42px; bottom: 28px;
    font-weight: 700;
    font-size: 11px;
    letter-spacing: 1px;
    color: var(--ink);
  }

  /* Front */
  .brand {
    position: absolute;
    left: 34px; top: 120px;
    display: flex; align-items: center; gap: 14px;
  }
  .brand-dot {
    width: 38px; height: 38px; border-radius: 50%;
    background: var(--accent);
  }
  .brand-name {
    font-weight: 900; font-size: 26px; letter-spacing: 2px; line-height: 1;
    color: var(--ink);
  }
  .brand-tagline {
    font-weight: 700; font-size: 8.5px; letter-spacing: .6px; margin-top: 3px;
  }
  .divider {
    position: absolute;
    left: 272px; top: 50px;
    width: 1px; height: 160px;
    background: var(--divider);
  }
  .contact {
    position: absolute;
    left: 292px; top: 48px;
  }
  .contact-name {
    font-weight: 700; font-size: 19px; color: var(--accent); letter-spacing: .5px;
  }
  .contact-title { font-size: 12px; color: var(--ink-soft); margin-bottom: 14px; }
  .contact-line {
    display: flex; align-items: center; gap: 8px;
    font-size: 12px; color: var(--ink); margin-bottom: 6px;
  }
  .contact-line svg { width: 12px; height: 12px; fill: var(--accent); flex: none; }
  .contact-address { font-size: 12px; color: var(--ink); margin-top: 12px; line-height: 1.4; padding-left: 20px; }
  .band-line {
    position: absolute; left: 0; right: 0; bottom: 50px; height: 3px;
    background: var(--accent);
  }
  .band {
    position: absolute; left: 0; right: 0; bottom: 0; height: 42px;
    background: var(--accent);
  }
  .band-dot {
    position: absolute; right: 70px; bottom: 28px;
    width: 36px; height: 36px; border-radius: 50%;
    background: var(--card); border: 4px solid var(--accent);
  }
</style>
</head>
<body>
  <section class="card card--back" aria-label="Card back">
    <div class="back-mark" aria-hidden="true"></div>
    <div class="back-name">QUORVANE</div>
    <div class="back-tagline">SENSING SYSTEMS</div>
  </section>

  <section class="card card--front" aria-label="Card front">
    <div class="brand">
      <span class="brand-dot" aria-hidden="true"></span>
      <div>
        <div class="brand-name">QUORVANE</div>
        <div class="brand-tagline">SENSING SYSTEMS</div>
      </div>
    </div>
    <div class="divider"></div>
    <div class="contact">
      <div class="contact-name">MARLENA OKAFOR</div>
      <div class="contact-title">Managing Director</div>
      <div class="contact-line">
        <svg viewBox="0 0 24 24"><path d="M6.6 10.8a15.1 15.1 0 0 0 6.6 6.6l2.2-2.2c.3-.3.7-.4 1-.2 1.1.4 2.3.6 3.6.6.6 0 1 .4 1 1V20c0 .6-.4 1-1 1A17 17 0 0 1 3 4c0-.6.4-1 1-1h3.5c.6 0 1 .4 1 1 0 1.3.2 2.5.6 3.6.1.3 0 .7-.2 1z"/></svg>
        044-555 010 274
      </div>
      <div class="contact-line">
        <svg viewBox="0 0 24 24"><path d="M2 5h20v14H2zm2 2v.5l8 5 8-5V7l-8 5z"/></svg>
        info@quorvane.com
      </div>
      <div class="contact-line">
        <svg viewBox="0 0 24 24"><path d="M12 2a10 10 0 1 0 0 20 10 10 0 0 0 0-20zm0 2c.9 1.2 1.6 2.6 2 4h-4c.4-1.4 1.1-2.8 2-4zM4.3 14a8 8 0 0 1 0-4h3.5a16 16 0 0 0 0 4zm.9 2h3a13 13 0 0 0 1.5 3.6A8 8 0 0 1 5.2 16zm3-8h-3a8 8 0 0 1 4.5-3.6A13 13 0 0 0 8.2 8zM12 20c-.9-1.2-1.6-2.6-2-4h4c-.4 1.4-1.1 2.8-2 4zm2.3-6H9.7a14 14 0 0 1 0-4h4.6a14 14 0 0 1 0 4zm.1 5.6A13 13 0 0 0 15.8 16h3a8 8 0 0 1-4.4 3.6zm1.8-5.6a16 16 0 0 0 0-4h3.5a8 8 0 0 1 0 4zm-.4-6a13 13 0 0 0-1.4-3.6A8 8 0 0 1 18.8 8z"/></svg>
        www.quorvanesense.com
      </div>
      <div class="contact-address">18 Harlow Street<br>70318, Norwen</div>
    </div>
    <div class="band-line"></div>
    <div class="band"></div>
    <div class="band-dot" aria-hidden="true"></div>
  </section>
</body>
</html>
```